real esate business card with company logo and name

we need a business card design for a real esate company

The company name is Walsh & Brody Pty Ltd, and we have our logo designed and will upload. We want classic or moden feel. Black or white background. looks more textured. Should include folowinginformations
Paul Walsh and Lucy Brody
Sales Agents & Onsite Manager
p: 07 5948 2063
F: 07 5948 2174
M:0461 857 239
3/42 Marlin Crescent, ELLEN GROVE QLD 4078

We want this business card looks professonal. Thank you in advance.

Industry/Entity Type

Real Estate Agent

Contact Information for Business Card

Paul Walsh and Lucy Brody
Onsite Manager & Sales Agents
p: 07 5948 2063
M:0461 857 239

Font styles to use
Serif

Colors
000000
fbfbfb
333333
959595

Requirements
Must have
• company logo and name, black or white back ground

```html
<!DOCTYPE html>
<html lang="en">
<head>
<meta charset="utf-8">
<title>Walsh &amp; Brody Pty Ltd — Business Card</title>
<link rel="stylesheet" href="https://fonts.googleapis.com/css2?family=Tinos:ital,wght@0,400;0,700;1,400&display=swap">
<style>
  :root {
    --page-bg: #ececec;
    --card-top: #5f5d5e;
    --card-bottom: #454344;
    --text-light: #fbfbfb;
    --text-soft: #e4e4e4;
    --brand-grey: #959595;
    --shadow: rgba(0, 0, 0, 0.28);
  }
  * { margin: 0; padding: 0; box-sizing: border-box; }
  html, body {
    width: 1200px;
    height: 1200px;
    overflow: hidden;
    background: var(--page-bg);
  }
  .stage {
    width: 1200px;
    height: 1200px;
    display: flex;
    align-items: center;
    justify-content: center;
  }
  .business-card {
    width: 500px;
    height: 820px;
    background: linear-gradient(170deg, var(--card-top) 0%, var(--card-bottom) 100%);
    box-shadow: 0 18px 40px var(--shadow);
    display: flex;
    flex-direction: column;
    align-items: center;
    font-family: "Tinos", "Times New Roman", serif;
    color: var(--text-light);
    text-align: center;
    padding-top: 170px;
  }
  .brand {
    display: flex;
    flex-direction: column;
    align-items: center;
    gap: 22px;
  }
  .brand-mark {
    width: 96px;
    height: 96px;
    border: 3px solid var(--brand-grey);
  }
  .brand-name {
    font-size: 22px;
    font-weight: 700;
    letter-spacing: 1px;
    color: var(--brand-grey);
    text-transform: uppercase;
  }
  .agents {
    margin-top: 72px;
    font-size: 29px;
    font-weight: 700;
    text-transform: uppercase;
    letter-spacing: 0.3px;
  }
  .role {
    margin-top: 12px;
    font-size: 25px;
    font-style: italic;
    color: var(--text-soft);
  }
  .contact {
    margin-top: 54px;
    list-style: none;
    font-size: 24px;
    line-height: 1.5;
  }
</style>
</head>
<body>
<main class="stage">
  <article class="business-card">
    <header class="brand">
      <div class="brand-mark" aria-hidden="true"></div>
      <p class="brand-name">Walsh &amp; Brody Pty Ltd.</p>
    </header>
    <h1 class="agents">Paul Walsh and Lucy Brody</h1>
    <p class="role">Onsite Manager &amp; Sales Agents</p>
    <ul class="contact">
      <li>p: 07 5948 2063</li>
      <li>M:0461 857 239</li>
      <li>3/42 Marlin Crescent,</li>
      <li>CORAL DOWNS QLD 4219</li>
    </ul>
  </article>
</main>
</body>
</html>
```